Business card for law firm

Need business card for new law firm. Think confident, authoritative, conservative, but not stuffy or old-fashioned.

Contact Information for Business Card

Content for card - logo (uploaded), plus the following:

Paul Wexbury (larger font)
Managing Partner (larger font, but not as large as name)
Level 9, 41 Tansy Lane
Sydney NSW 2000
Main Tel 02 7346 2190
Direct Tel 02 6273 4415
Email paul@qvlegal.com.au
www.qvlegal.com.au

Letterhead design should include logo plus:
Level 9, 41 Tansy Lane
Sydney NSW 2000
Tel 02 6273 4415
www.qvlegal.com.au

```html
<!DOCTYPE html>
<html lang="en">
<head>
<meta charset="utf-8">
<title>Quayvale Legal – Stationery</title>
<link rel="stylesheet" href="https://fonts.googleapis.com/css2?family=PT+Sans:wght@400;700&display=swap">
<style>
  :root {
    --canvas: #e4e2e3;
    --navy: #1f2352;
    --ink: #231f20;
    --paper: #ffffff;
    --mark: #15205a;
    --faint: #ebebeb;
    --light-text: #ffffff;
  }
  * { box-sizing: border-box; margin: 0; padding: 0; }
  html, body { width: 1200px; height: 1200px; overflow: hidden; }
  body {
    position: relative;
    background: var(--canvas);
    font-family: "PT Sans", Arial, sans-serif;
    color: var(--ink);
  }

  /* Brand lock-up */
  .brand { position: absolute; display: flex; flex-direction: column; align-items: center; }
  .brand-square { background: var(--mark); }
  .brand-name { color: var(--mark); font-weight: 400; white-space: nowrap; letter-spacing: 0.04em; }

  .brand--hero { left: 56px; top: 54px; width: 224px; }
  .brand--hero .brand-square { width: 52px; height: 52px; margin-bottom: 26px; }
  .brand--hero .brand-name { font-size: 33px; }

  /* Business card */
  .card {
    position: absolute; left: 97px; width: 322px; height: 189px;
    background: var(--paper); overflow: hidden;
  }
  .card--one { top: 491px; }
  .card--two { top: 791px; }
  .card-panel {
    position: absolute; inset: 0;
    background: var(--navy);
    clip-path: polygon(0 0, 204px 0, 157px 100%, 0 100%);
  }
  .card-name {
    position: absolute; left: 0; width: 196px; top: 22px;
    text-align: center; color: var(--light-text);
    font-weight: 700; font-size: 21px; line-height: 1;
  }
  .card-role {
    position: absolute; left: 0; width: 192px; top: 51px;
    text-align: center; color: var(--light-text);
    font-size: 12px; line-height: 1;
  }
  .pill {
    position: absolute; left: 0; height: 16px;
    background: var(--ink); border-radius: 0 8px 8px 0;
  }
  .pill svg { position: absolute; top: 3px; width: 10px; height: 10px; fill: var(--light-text); }
  .pill-text {
    position: absolute; color: var(--light-text);
    font-weight: 700; font-size: 7.5px; line-height: 10px; white-space: nowrap;
  }
  .card .brand { left: 200px; width: 90px; top: 43px; }
  .card .brand-square { width: 18px; height: 20px; margin-bottom: 10px; }
  .card .brand-name { font-size: 11.5px; }
  .card-web, .card-email {
    position: absolute; left: 200px; width: 90px; text-align: center;
    font-weight: 700; font-size: 9.5px; white-space: nowrap; color: var(--ink);
  }
  .card-web { top: 117px; }
  .card-email { top: 141px; left: 195px; width: 100px; font-size: 8.6px; }

  /* Letterhead */
  .letterhead {
    position: absolute; left: 519px; top: 287px; width: 592px; height: 831px;
    background: var(--paper); overflow: hidden;
  }
  .lh-topband { position: absolute; left: 0; top: 0; width: 100%; height: 18px; background: var(--navy); border-bottom: 3px solid var(--ink); height: 21px; }
  .letterhead .brand { left: 196px; width: 202px; top: 41px; }
  .letterhead .brand-square { width: 40px; height: 48px; margin-bottom: 24px; }
  .letterhead .brand-name { font-size: 27px; }
  .lh-emblem {
    position: absolute; left: 69px; top: 257px; width: 454px; height: 314px;
    background: var(--faint); border-radius: 40px 40px 10px 10px;
  }
  .lh-footer {
    position: absolute; left: 0; top: 719px; width: 100%; height: 112px;
    background: var(--navy); border-top: 4px solid var(--ink);
  }
  .lh-footer .pill { height: 20px; border-radius: 0 10px 10px 0; }
  .lh-footer .pill svg { top: 4px; width: 12px; height: 12px; }
  .lh-footer .pill-text { font-weight: 400; font-size: 11px; line-height: 13px; }
  .lh-web {
    position: absolute; left: 275px; top: 32px; width: 250px;
    color: var(--light-text); font-size: 27px; letter-spacing: 0.07em; white-space: nowrap;
  }
</style>
</head>
<body>

<svg width="0" height="0" style="position:absolute">
  <defs>
    <symbol id="icon-home" viewBox="0 0 12 12"><path d="M6 1 L11.5 6 H10 V11 H7.3 V8 H4.7 V11 H2 V6 H0.5 Z"/></symbol>
    <symbol id="icon-phone" viewBox="0 0 12 12"><path d="M2.4 0.8 L4.4 3.2 L3.3 4.6 C4 6 5.8 7.8 7.3 8.6 L8.7 7.5 L11.2 9.5 L9.8 11.2 C5.6 11 0.9 6.3 0.8 2.2 Z"/></symbol>
  </defs>
</svg>

<div class="brand brand--hero">
  <div class="brand-square"></div>
  <div class="brand-name">Quayvale Legal</div>
</div>

<div class="card card--one">
  <div class="card-panel"></div>
  <div class="card-name">Paul Wexbury</div>
  <div class="card-role">Managing Partner</div>
  <div class="pill" style="top:86px;width:66px"><svg style="left:45px"><use href="#icon-home"/></svg></div>
  <div class="pill-text" style="left:74px;top:89px">Level 9, 41 Tansy Lane<br>Sydney NSW 2000</div>
  <div class="pill" style="top:120px;width:54px"><svg style="left:35px"><use href="#icon-phone"/></svg></div>
  <div class="pill-text" style="left:62px;top:124px">Main Tel 02 7346 2190</div>
  <div class="pill" style="top:148px;width:43px"><svg style="left:25px"><use href="#icon-phone"/></svg></div>
  <div class="pill-text" style="left:52px;top:152px">Direct Tel 02 6273 4415</div>
  <div class="brand"><div class="brand-square"></div><div class="brand-name">Quayvale Legal</div></div>
  <div class="card-web">www.qvlegal.com.au</div>
  <div class="card-email">Email paul@qvlegal.com.au</div>
</div>

<div class="card card--two">
  <div class="card-panel"></div>
  <div class="card-name">Paul Wexbury</div>
  <div class="card-role">Managing Partner</div>
  <div class="pill" style="top:86px;width:66px"><svg style="left:45px"><use href="#icon-home"/></svg></div>
  <div class="pill-text" style="left:74px;top:89px">Level 9, 41 Tansy Lane<br>Sydney NSW 2000</div>
  <div class="pill" style="top:120px;width:54px"><svg style="left:35px"><use href="#icon-phone"/></svg></div>
  <div class="pill-text" style="left:62px;top:124px">Main Tel 02 7346 2190</div>
  <div class="pill" style="top:148px;width:43px"><svg style="left:25px"><use href="#icon-phone"/></svg></div>
  <div class="pill-text" style="left:52px;top:152px">Direct Tel 02 6273 4415</div>
  <div class="brand"><div class="brand-square"></div><div class="brand-name">Quayvale Legal</div></div>
  <div class="card-web">www.qvlegal.com.au</div>
  <div class="card-email">Email paul@qvlegal.com.au</div>
</div>

<div class="letterhead">
  <div class="lh-topband"></div>
  <div class="brand"><div class="brand-square"></div><div class="brand-name">Quayvale Legal</div></div>
  <div class="lh-emblem" role="img" aria-label="Faint watermark illustration of the scales of justice"></div>
  <div class="lh-footer">
    <div class="pill" style="top:22px;width:68px"><svg style="left:43px"><use href="#icon-home"/></svg></div>
    <div class="pill-text" style="left:83px;top:22px">Level 9, 41 Tansy Lane<br>Sydney NSW 2000</div>
    <div class="pill" style="top:62px;width:68px"><svg style="left:43px"><use href="#icon-phone"/></svg></div>
    <div class="pill-text" style="left:84px;top:66px;font-size:12px">Tel 02 6273 4415</div>
    <div class="lh-web">www.qvlegal.com.au</div>
  </div>
</div>

</body>
</html>
```